MAVO VERTICAL & HORIZONTAL FOLDING STICKERS FOR PACKAGING

We are a California Dispensary that will be launching our marijuana brands. We would like to use the MAVO logo developed (attached) for one of our flower brands. We love the look and feel and believe it will provide great branding for us.

This product will be in black and clear bags for display at stores.

For the Bags, we will need vertical and horizontal packaging for our stickers. IMPORTANT TO NOTE, these stickers will be folding the stickers AROUND THE BAGS.

Additionally, there are restrictions about what needs to be on the package; a separate document is included with that information along with some examples.

For the VERTICAL STICKERS, we will be folding the strip to cover part of the front of the bag and part of the back of the bag. The front part should represent 70% of the label, and the back part (folded over) should be 30%. Please keep the warnings on the back.

For the HORIZONTAL, the fold will be broken out as 75% to 80% on the front of the bag, and 20 to 25% on the back of the bag.
For both VERTICAL AND HORIZONTAL, please keep the warnings on the back. Note, that we would like the strain name (e.g.: Amber Drift) to be very visible on the front of both of these.

The three sticker colors are glossy white, silver, and gold. If you choose to focus on the white sticker, please be sure to incorporate background color as you see fit to ensure the logo and packaging will pop on the shelves.

Sticker sizes are below for use in development of this packaging:
Roll Label: 5" x 2" High Gloss White Polypropylene (BOPP) (R31).
SQUARE CORNERS - 1300 labels per roll - 0.0156" corner radius - 0.125"gap (top / bottom), 0.0625"margin (left / right) - 3" core, 6" outside - minimum quantity 1
__
One item we like from the Ferrow Cannabis label example is the approach to the strain (hybrid, sativa, Indica). We will also have a strain name (eg: Amber Drift). I've enclosed picture examples but would be happy to provide more information.

```html
<!DOCTYPE html>
<html lang="en">
<head>
<meta charset="utf-8">
<title>MAVO – Amber Drift horizontal label</title>
<link rel="stylesheet" href="https://fonts.googleapis.com/css2?family=Anton&family=Quicksand:wght@500;700&family=Roboto+Condensed:wght@400;500;700&display=swap">
<style>
  :root{
    --page:#ffffff;
    --label:#000000;
    --text:#ffffff;
    --green:#8cc63f;
    --gold-light:#f6e39a;
    --gold:#e0b34a;
    --gold-dark:#9a6a1c;
    --alert:#f7c51e;
  }
  *{margin:0;padding:0;box-sizing:border-box}
  html,body{width:1200px;height:1007px;overflow:hidden;background:var(--page)}
  .label{
    position:absolute;left:143px;top:320px;width:915px;height:366px;
    background:var(--label);color:var(--text);
  }
  .gov-warning{
    position:absolute;left:23px;top:23px;width:240px;
    font-family:"Roboto Condensed",sans-serif;font-size:11.4px;line-height:14.4px;
    text-align:justify;text-align-last:justify;text-transform:uppercase;
  }
  .gov-warning .gov-warning__lead{font-weight:700}
  .gov-warning p:last-child{text-align-last:left}
  .prop-warning{
    position:absolute;left:23px;top:252px;width:240px;text-align:center;
    font-family:"Quicksand",sans-serif;font-size:12.4px;line-height:13.4px;font-weight:500;
  }
  .prop-warning__icon{display:block;margin:0 auto 2px;width:52px;height:47px}
  .prop-warning__title{font-weight:700;font-size:12px;letter-spacing:.3px}
  .brand{
    position:absolute;left:357px;top:36px;width:200px;text-align:center;
    font-family:"Quicksand",sans-serif;font-weight:700;font-size:48px;line-height:1;
    color:var(--green);letter-spacing:1px;
  }
  .strain{
    position:absolute;left:345px;top:128px;width:230px;text-align:center;
    font-family:"Anton",sans-serif;font-size:81px;line-height:73px;letter-spacing:2px;
  }
  .strain__first{color:var(--green);display:block}
  .strain__second{
    display:block;
    background:linear-gradient(90deg,var(--gold) 0%,var(--gold-light) 30%,var(--gold) 55%,var(--gold-light) 75%,var(--gold-dark) 100%);
    -webkit-background-clip:text;background-clip:text;color:transparent;
  }
  .net-weight{
    position:absolute;left:344px;top:317px;width:100px;text-align:center;
    font-family:"Quicksand",sans-serif;font-size:13.5px;line-height:16px;color:var(--gold);
  }
  .net-weight__amount{font-size:15px}
  .compliance-badge{position:absolute;left:492px;top:291px;width:58px;height:64px}
  .description{
    position:absolute;left:659px;top:30px;width:236px;text-align:center;
    font-family:"Quicksand",sans-serif;font-weight:500;font-size:12.3px;line-height:16.9px;
  }
</style>
</head>
<body>
<section class="label">
  <div class="gov-warning">
    <p><span class="gov-warning__lead">Government warning:</span> This product contains cannabis, a schedule I controlled substance. Keep out of reach of children and animals. Cannabis products may only be possessed or consumed by persons 21 years of age or older unless the person is a qualified patient. The intoxicating effects of cannabis products may be delayed up to two hours. Cannabis use while pregnant or breastfeeding may be harmful. Consumption of cannabis products impairs your ability to drive and operate machinery. Please use extreme caution.</p>
  </div>

  <div class="prop-warning">
    <svg class="prop-warning__icon" viewBox="0 0 52 47" aria-hidden="true">
      <path d="M26 3 L49 43 H3 Z" fill="var(--alert)" stroke="var(--alert)" stroke-width="4" stroke-linejoin="round"/>
      <path d="M26 7 L45 41 H7 Z" fill="none" stroke="#000" stroke-width="2" stroke-linejoin="round"/>
      <rect x="23.5" y="15" width="5" height="16" rx="2" fill="#000"/>
      <circle cx="26" cy="36" r="2.8" fill="#000"/>
    </svg>
    <div class="prop-warning__title">WARNING</div>
    <div>Cancer and reproductive harm.</div>
    <div>www.prop-notice.example.org</div>
  </div>

  <div class="brand">MAVO</div>

  <h1 class="strain">
    <span class="strain__first">AMBER</span>
    <span class="strain__second">DRIFT</span>
  </h1>

  <div class="net-weight">
    <div>NET WT</div>
    <div class="net-weight__amount">1/4oz (7g)</div>
  </div>

  <svg class="compliance-badge" viewBox="0 0 58 64" aria-label="Compliance badge">
    <path d="M29 4 L54 44 H4 Z" fill="none" stroke="var(--gold)" stroke-width="4" stroke-linejoin="round"/>
  </svg>

  <p class="description">Lorem ipsum dolor sit amet, consectetur adipiscing elit. Mauris eu eros tellus. Aenean ac lacus ut ante dictum blandit. In commodo tempus mi, quis aliquet est hendrerit vel. Quisque at metus nibh. Phasellus vehicula sem tortor, sit amet fermentum dolor pretium et. Proin eget elit sed ligula venenatis maximus ac id nulla. Vivamus non nisi lacus. Aenean nisi diam, facilisis eget sollicitudin ut, ultricies hendrerit leo. Lorem ipsum dolor sit amet, consectetur adipiscing elit. Proin a volutpat nibh. Class aptent taciti sociosqu ad litora torquent per conubia nostra, per inceptos himenaeos.</p>
</section>
</body>
</html>
```